Property developer, money partner needs business card design using logo concept provided

Our company develops residential properties, does money lends for joint ventures in property deals and finds property deals for other money partners. We have provided a basic logo for you to work from. Any graphic or logo design on the card is to communicate development and finance collaboration. Color choice is not so important for us, but color choice does need to reflect professionalism.

```html
<!DOCTYPE html>
<html lang="en">
<head>
<meta charset="utf-8">
<title>Brickleaf Property Partners – Business Card</title>
<link rel="stylesheet" href="https://fonts.googleapis.com/css2?family=Montserrat:wght@600;700;800&family=Lato:wght@400;700&display=swap">
<style>
  :root{
    --bg:#2b2b2d;
    --blue-light:#0677bd;
    --blue-dark:#053f86;
    --blue-text:#0b63b3;
    --red:#a01d22;
    --ink:#1d1d1d;
    --white:#ffffff;
    --line:#2a78c2;
  }
  *{box-sizing:border-box;margin:0;padding:0}
  html,body{width:1200px;height:875px;overflow:hidden}
  body{background:var(--bg);display:flex;align-items:center;justify-content:center;gap:40px}
  .card{width:540px;height:310px;border-radius:26px;position:relative;overflow:hidden;box-shadow:0 18px 40px rgba(0,0,0,.45)}
  .card--front{background:linear-gradient(160deg,var(--blue-light) 0%,var(--blue-dark) 100%);display:flex;flex-direction:column;align-items:center;justify-content:center;color:var(--white)}
  .brand{display:flex;align-items:center;gap:12px;font-family:"Montserrat",sans-serif;font-weight:800;letter-spacing:.14em}
  .brand__dot{width:22px;height:22px;border-radius:50%;background:currentColor;flex:none}
  .card--front .brand{font-size:30px}
  .acn{font-family:"Montserrat",sans-serif;font-weight:600;font-size:10px;letter-spacing:.2em;margin-top:12px}
  .card--back{background:var(--white);display:flex;align-items:center;padding:0 34px}
  .back__brand{width:200px;display:flex;flex-direction:column;align-items:center;color:var(--blue-text)}
  .card--back .brand{font-size:19px;gap:8px}
  .card--back .brand__dot{width:14px;height:14px}
  .card--back .acn{font-size:8px;color:var(--red);margin-top:8px}
  .divider{width:2px;height:190px;background:var(--line);margin:0 26px 0 14px;flex:none}
  .details{font-family:"Lato",sans-serif;color:var(--ink)}
  .details__name{font-family:"Montserrat",sans-serif;font-weight:800;font-size:26px;color:var(--blue-text);letter-spacing:.01em;line-height:1}
  .details__title{font-family:"Lato",sans-serif;font-size:15px;color:var(--red);margin:4px 0 14px}
  .contact{list-style:none;font-size:12px;line-height:1.5}
  .contact li{display:flex;align-items:flex-start;gap:9px}
  .contact li + li{margin-top:2px}
  .contact__address{margin-bottom:6px}
  .icon{width:11px;height:11px;fill:var(--red);flex:none;margin-top:3px}
</style>
</head>
<body>
  <section class="card card--front" aria-label="Card front">
    <div class="brand"><span class="brand__dot"></span>BRICKLEAF</div>
    <div class="acn">A.C.N 481 302 916</div>
  </section>

  <section class="card card--back" aria-label="Card back">
    <div class="back__brand">
      <div class="brand"><span class="brand__dot"></span>BRICKLEAF</div>
      <div class="acn">A.C.N 481 302 916</div>
    </div>
    <div class="divider"></div>
    <div class="details">
      <h1 class="details__name">DANIEL REYES</h1>
      <p class="details__title">Founder &amp; CEO</p>
      <ul class="contact">
        <li class="contact__address">
          <svg class="icon" viewBox="0 0 12 12"><path d="M6 0a4 4 0 0 0-4 4c0 3 4 8 4 8s4-5 4-8a4 4 0 0 0-4-4zm0 5.6A1.6 1.6 0 1 1 6 2.4a1.6 1.6 0 0 1 0 3.2z"/></svg>
          <span>Your Address, City<br>State, Country, Zip 1235</span>
        </li>
        <li>
          <svg class="icon" viewBox="0 0 12 12"><path d="M2.4 0 4.4 2.6 3.2 4a7 7 0 0 0 4.8 4.8L9.4 7.6 12 9.6 10.6 12C5 11.6.4 7 0 1.4z"/></svg>
          <span>(123) 456-7890</span>
        </li>
        <li>
          <svg class="icon" viewBox="0 0 12 12"><path d="M3 0h6a1 1 0 0 1 1 1v10a1 1 0 0 1-1 1H3a1 1 0 0 1-1-1V1a1 1 0 0 1 1-1zm.6 1.4v8h4.8v-8z"/></svg>
          <span>(231) 456-7890</span>
        </li>
        <li>
          <svg class="icon" viewBox="0 0 12 12"><path d="M3 0h6v3H3zM1 4h10a1 1 0 0 1 1 1v4H10v3H2V9H0V5a1 1 0 0 1 1-1zm2.4 5v1.6h5.2V9z"/></svg>
          <span>(312) 456-7890</span>
        </li>
        <li>
          <svg class="icon" viewBox="0 0 12 12"><path d="M0 2h12v1L6 7 0 3zm0 2.4 6 4 6-4V10H0z"/></svg>
          <span>office@yourwebsite.com</span>
        </li>
        <li>
          <svg class="icon" viewBox="0 0 12 12"><path d="M6 0a6 6 0 1 0 0 12A6 6 0 0 0 6 0zm0 1.3c.8 0 1.6 1.7 1.7 4H4.3c.1-2.3.9-4 1.7-4zM1.3 6.7h1.8c.1 1.5.4 2.8.9 3.6A4.8 4.8 0 0 1 1.3 6.7zm0-1.4A4.8 4.8 0 0 1 4 1.7c-.5.8-.8 2.1-.9 3.6zM6 10.7c-.8 0-1.6-1.7-1.7-4h3.4c-.1 2.3-.9 4-1.7 4zm2-.4c.5-.8.8-2.1.9-3.6h1.8A4.8 4.8 0 0 1 8 10.3zm.9-5c-.1-1.5-.4-2.8-.9-3.6a4.8 4.8 0 0 1 2.7 3.6z"/></svg>
          <span>www.yourwebsite.com</span>
        </li>
      </ul>
    </div>
  </section>
</body>
</html>
```